Varnel needs a Powerpoint and Google Slides Template!

We need elegant, smart, clear templates for our powerpoint and google slides documents. They should use our logo, fonts, etc, and be technically proficient (e.g. fonts show up in tables, etc).

Attached is our current powerpoint template, which is uninspired, our logo, and our guidelines. Glad to provide other useful tools.

Target Market(s)

Educators (both K12 and higher ed)

Industry/Entity Type

Google

Font styles to use
Sans Serif

Requirements
Must have
• Clean look and feel. All fonts and page layouts consistent and working.

```html
<!DOCTYPE html>
<html lang="en">
<head>
<meta charset="utf-8">
<title>Varnel Presentation Template</title>
<link href="https://fonts.googleapis.com/css2?family=Open+Sans:wght@300;400;600;700&display=swap" rel="stylesheet">
<style>
:root{
  --cyan:#27b4e2;
  --cyan-dark:#1b9bc6;
  --cyan-soft:#d6f0fa;
  --ink:#4a4a4a;
  --muted:#8d8d8d;
  --line:#e3e3e3;
  --grey:#9a9a9a;
  --dark:#3c4449;
  --page:#ececec;
}
*{box-sizing:border-box;margin:0;padding:0}
html,body{width:1200px;height:3919px;overflow:hidden;background:var(--page)}
body{font-family:"Open Sans",Arial,sans-serif;color:var(--ink)}
.deck{display:grid;grid-template-columns:repeat(3,392px);grid-auto-rows:219px;gap:11px 12px;padding:10px 0;width:1200px;height:3919px}
.slide{position:relative;background:#fff;overflow:hidden;box-shadow:0 0 0 1px #dcdcdc}
.abs{position:absolute}
.photo{position:absolute;background:linear-gradient(135deg,#c7d5dd,#eef2f5)}
.photo.warm{background:linear-gradient(135deg,#d8c2ad,#f1e6db)}
.photo.dark{background:linear-gradient(135deg,#323b40,#5b676c)}
.photo.cool{background:linear-gradient(135deg,#9fd9ef,#dff3fb)}
.photo.tint{background:linear-gradient(135deg,rgba(39,180,226,.9),rgba(120,210,240,.75))}
.foot{position:absolute;left:0;right:0;bottom:0;height:9px;background:var(--cyan);color:#fff;font-size:4px;line-height:9px;padding-left:10px}
.foot .num{position:absolute;right:6px;top:0;width:9px;height:9px;background:#fff;color:var(--cyan);text-align:center}
.mark{position:absolute;top:8px;right:10px;font-size:7px;font-weight:700;color:var(--cyan);display:flex;align-items:center;gap:3px;letter-spacing:.3px}
.mark::before{content:"";width:7px;height:7px;border-radius:50%;background:var(--cyan)}
.mark.light{color:#fff}
.mark.light::before{background:#fff}
.brand{display:flex;align-items:center;gap:8px;color:#fff;font-weight:700;letter-spacing:1px}
.brand .disc{border-radius:50%;background:#fff;flex:none}
.ttl{position:absolute;left:14px;top:12px;font-size:10px;color:var(--ink)}
.ttl.w{color:#fff}
.sh{font-size:6px;font-weight:600;color:var(--cyan);line-height:8px}
.sh.ink{color:var(--ink)}
.p{font-size:4.5px;line-height:6.5px;color:var(--muted)}
.p.w{color:#eaf8fd}
.hl{font-size:7px;line-height:9px;color:var(--ink)}
.hl b{color:var(--cyan);font-weight:600}
.ci{display:inline-flex;align-items:center;justify-content:center;width:11px;height:11px;border-radius:50%;background:var(--cyan);flex:none}
.ci svg{width:6px;height:6px}
.sq{display:inline-flex;align-items:center;justify-content:center;width:11px;height:11px;background:var(--cyan);color:#fff;font-size:5px;font-weight:700;flex:none}
.row{display:flex;gap:5px;align-items:flex-start}
.cyanbg{background:var(--cyan)}
.big-quote{font-size:9px;line-height:12px;color:var(--ink)}
table{border-collapse:collapse;width:100%}
</style>
</head>
<body>
<main class="deck">

<!-- 1 cover -->
<section class="slide">
  <div class="photo cool" style="inset:0" role="img" aria-label="Bright classroom background in cyan tones"></div>
  <div class="abs" style="left:40px;top:70px">
    <div class="brand" style="font-size:26px"><span class="disc" style="width:34px;height:34px"></span>VARNEL</div>
    <div style="color:#fff;font-size:8px;margin-top:8px;margin-left:2px">Choose Better. Learn Better.</div>
  </div>
</section>

<!-- 2 title with presenters -->
<section class="slide">
  <div class="photo" style="left:0;top:0;width:392px;height:118px" role="img" aria-label="Student writing in a notebook"></div>
  <div class="abs cyanbg" style="left:60px;top:92px;width:272px;height:38px;text-align:center;color:#fff">
    <div style="font-size:12px;margin-top:5px">Your Title Goes Here</div>
    <div style="font-size:5px;margin-top:2px">Your Subtitle Goes Here</div>
  </div>
  <div class="abs" style="left:40px;top:150px;right:40px;display:flex;justify-content:space-between">
    <div class="row"><span class="ci" style="background:#cfd8dd"></span><div><div class="sh ink">Alex Reed</div><div class="p">Job Title</div></div></div>
    <div class="row"><span class="ci" style="background:#cfd8dd"></span><div><div class="sh ink">Mia Lane</div><div class="p">Job Title</div></div></div>
    <div class="row"><span class="ci" style="background:#cfd8dd"></span><div><div class="sh ink">Sam Cole</div><div class="p">Job Title</div></div></div>
  </div>
  <div class="foot" style="height:6px"></div>
</section>

<!-- 3 title band -->
<section class="slide">
  <div class="photo" style="left:0;top:0;width:392px;height:120px" role="img" aria-label="Students studying together at a desk"></div>
  <div class="mark">VARNEL</div>
  <div class="abs cyanbg" style="left:0;top:108px;width:392px;height:30px"></div>
  <div class="abs" style="right:20px;top:113px;color:#fff;font-size:12px;text-align:right">Your Title Goes Here<div style="font-size:5px">Your Subtitle Goes Here</div></div>
  <div class="abs p" style="left:20px;top:170px">Presented by Alex Reed</div>
  <div class="abs p" style="right:20px;top:170px">Date of presentation here</div>
  <div class="foot" style="height:6px"></div>
</section>

<!-- 4 graduate title -->
<section class="slide">
  <div class="photo" style="left:0;top:0;width:392px;height:219px" role="img" aria-label="Graduate in cap holding a sign"></div>
  <div class="abs" style="left:36px;top:60px;width:60px;height:60px;border-radius:50%;background:#fff;box-shadow:0 0 0 4px var(--cyan)"></div>
  <div class="abs cyanbg" style="left:160px;top:0;width:232px;height:219px"></div>
  <div class="mark light" style="left:172px;right:auto;top:40px;font-size:10px">VARNEL</div>
  <div class="abs" style="left:176px;top:90px;color:#fff;font-size:13px">Your Title Goes Here</div>
  <div class="abs p w" style="left:176px;top:108px">Your subtitle goes here</div>
  <div class="abs" style="left:270px;top:140px;color:#fff;font-size:5px;text-align:center">Presented by<div style="font-size:7px;font-weight:600">Nora Vale</div><div>Job Title</div></div>
</section>

<!-- 5 agenda -->
<section class="slide">
  <div class="ttl">Our Agenda</div><div class="mark">VARNEL</div>
  <div class="abs" style="left:24px;top:42px;width:340px;display:grid;grid-template-columns:1fr 1fr;gap:18px 40px">
    <div class="row"><span class="sq">1</span><div><div class="sh ink">Agenda One</div><div class="p">Short note on this agenda topic.</div></div></div>
    <div class="row"><span class="sq">4</span><div><div class="sh ink">Agenda Four</div><div class="p">Short note on this agenda topic.</div></div></div>
    <div class="row"><span class="sq">2</span><div><div class="sh ink">Agenda Two</div><div class="p">Short note on this agenda topic.</div></div></div>
    <div class="row"><span class="sq">5</span><div><div class="sh ink">Agenda Five</div><div class="p">Short note on this agenda topic.</div></div></div>
    <div class="row"><span class="sq">3</span><div><div class="sh ink">Agenda Three</div><div class="p">Short note on this agenda topic.</div></div></div>
    <div class="row"><span class="sq">6</span><div><div class="sh ink">Agenda Six</div><div class="p">Short note on this agenda topic.</div></div></div>
  </div>
  <div class="foot">Copyright Varnel<span class="num">5</span></div>
</section>

<!-- 6 about -->
<section class="slide">
  <div class="ttl">About Varnel</div><div class="mark">VARNEL</div>
  <div class="abs" style="left:14px;top:34px;width:200px">
    <div class="sh">We are Varnel</div>
    <div class="hl" style="margin:2px 0 5px"><b>Choose Better. Learn Better.</b></div>
    <div class="sh ink">Who We Are</div>
    <div class="p" style="margin-bottom:5px">We build clear learning tools for classrooms, campuses and teachers who want simple, lasting results every single day.</div>
    <div class="sh ink">What We Do</div>
    <div class="p">We help schools plan, teach and review lessons with tools that stay out of the way and let learners focus.</div>
  </div>
  <div class="photo" style="left:232px;top:34px;width:146px;height:166px" role="img" aria-label="Smiling man in a suit"></div>
  <div class="foot">Copyright Varnel<span class="num">6</span></div>
</section>

<!-- 7 title goes here with photo -->
<section class="slide">
  <div class="photo warm" style="left:0;top:0;width:190px;height:210px" role="img" aria-label="Family reading together"></div>
  <div class="abs" style="left:204px;top:28px;width:170px">
    <div class="hl" style="font-size:9px"><b>Title</b> Goes Here</div>
    <div class="p" style="margin-top:5px">Add a short paragraph of body text here to describe this point for your audience in plain words.</div>
  </div>
  <div class="abs cyanbg" style="left:196px;top:110px;width:186px;height:80px;padding:10px">
    <div class="p w">Add a short paragraph of body text here to describe this point for your audience in plain words and clear terms.</div>
  </div>
  <div class="foot">Copyright Varnel<span class="num">7</span></div>
</section>

<!-- 8 vision mission -->
<section class="slide cyanbg">
  <div class="ttl w">Our Vision &amp; Mission</div><div class="mark light">VARNEL</div>
  <div class="abs" style="left:20px;top:48px;width:160px;color:#fff">
    <div class="sh" style="color:#fff">Our Vision</div>
    <div style="font-size:8px;line-height:10px;margin:4px 0">Go to the Next Level Without look in the past</div>
    <div class="p w">Add a short paragraph of body text here to describe the vision of the team.</div>
  </div>
  <div class="abs" style="left:205px;top:48px;width:170px;color:#fff">
    <div class="sh" style="color:#fff">Our Missions</div>
    <div class="row" style="margin-top:6px"><span class="ci" style="background:#fff"></span><div><div class="sh" style="color:#fff">Your Text Here</div><div class="p w">Short supporting line here.</div></div></div>
    <div class="row" style="margin-top:6px"><span class="ci" style="background:#fff"></span><div><div class="sh" style="color:#fff">Your Text Here</div><div class="p w">Short supporting line here.</div></div></div>
    <div class="row" style="margin-top:6px"><span class="ci" style="background:#fff"></span><div><div class="sh" style="color:#fff">Your Text Here</div><div class="p w">Short supporting line here.</div></div></div>
  </div>
  <div class="foot" style="background:#1f9ecb">Copyright Varnel<span class="num">8</span></div>
</section>

<!-- 9 quote -->
<section class="slide">
  <div class="ttl">Quote Area</div><div class="mark">VARNEL</div>
  <div class="abs" style="left:20px;top:62px;width:170px">
    <div class="big-quote" style="color:var(--cyan)">&ldquo; Education is the most powerful weapon which you can use to change the world.</div>
    <div class="p" style="margin-top:6px">Ruth Calder</div>
  </div>
  <div class="photo" style="left:200px;top:30px;width:180px;height:170px" role="img" aria-label="Students smiling in a classroom"></div>
  <div class="foot">Copyright Varnel<span class="num">9</span></div>
</section>

<!-- 10 text area -->
<section class="slide">
  <div class="ttl">Text Area</div>
  <div class="abs" style="left:14px;top:40px;width:180px">
    <div class="hl">We are <b>Varnel</b><br>Choose Better. Learn Better.</div>
    <div class="p" style="margin-top:6px">Add a short paragraph of body text here to describe this point for your audience.</div>
    <div class="p" style="margin-top:6px">Add a second paragraph of body text here to expand on the point above.</div>
  </div>
  <div class="abs cyanbg" style="left:210px;top:0;width:182px;height:219px;padding:30px 16px">
    <div class="brand" style="font-size:13px"><span class="disc" style="width:16px;height:16px"></span>VARNEL</div>
    <div class="p w" style="margin-top:14px">Add a short paragraph of body text here to describe this point for your audience in plain words.</div>
  </div>
</section>

<!-- 11 three photos -->
<section class="slide">
  <div class="ttl">Your Title Goes Here</div><div class="mark">VARNEL</div>
  <div class="photo" style="left:14px;top:34px;width:114px;height:70px" role="img" aria-label="Students in a lecture"></div>
  <div class="photo tint" style="left:139px;top:34px;width:114px;height:70px" role="img" aria-label="Students at laptops"></div>
  <div class="photo" style="left:264px;top:34px;width:114px;height:70px" role="img" aria-label="Teacher helping a student"></div>
  <div class="abs" style="left:14px;top:114px;width:364px;display:grid;grid-template-columns:repeat(3,1fr);gap:11px">
    <div><div class="sh ink">Heading Goes Here</div><div class="p">Add a short line of body text here to describe this point.</div></div>
    <div><div class="sh ink">Heading Goes Here</div><div class="p">Add a short line of body text here to describe this point.</div></div>
    <div><div class="sh ink">Heading Goes Here</div><div class="p">Add a short line of body text here to describe this point.</div></div>
  </div>
  <div class="foot">Copyright Varnel<span class="num">11</span></div>
</section>

<!-- 12 text area photos -->
<section class="slide">
  <div class="ttl">Text Area</div><div class="mark">VARNEL</div>
  <div class="abs" style="left:14px;top:36px;width:190px">
    <div class="hl">We are <b>Varnel</b><br>Choose Better. Learn Better.</div>
    <div class="p" style="margin-top:6px">Add a short paragraph of body text here to describe this point for your audience.</div>
    <div class="p" style="margin-top:6px">Add a second paragraph of body text here to expand on the point above.</div>
  </div>
  <div class="photo warm" style="left:218px;top:36px;width:160px;height:80px" role="img" aria-label="Children reading books"></div>
  <div class="photo" style="left:218px;top:122px;width:160px;height:78px" role="img" aria-label="Students at a table"></div>
  <div class="foot">Copyright Varnel<span class="num">12</span></div>
</section>

<!-- 13 boy with list -->
<section class="slide">
  <div class="photo" style="left:0;top:0;width:150px;height:219px" role="img" aria-label="Boy with glasses writing"></div>
  <div class="abs" style="left:162px;top:24px;width:210px">
    <div class="hl">We are <b>Varnel</b><br>Choose Better. Learn Better.</div>
    <div class="row" style="margin-top:10px"><span class="ci"></span><div class="p">Add a short line of body text here for this point.</div></div>
    <div class="row" style="margin-top:8px"><span class="ci"></span><div class="p">Add a short line of body text here for this point.</div></div>
    <div class="row" style="margin-top:8px"><span class="ci"></span><div class="p">Add a short line of body text here for this point.</div></div>
    <div class="row" style="margin-top:8px"><span class="ci"></span><div class="p">Add a short line of body text here for this point.</div></div>
  </div>
  <div class="foot" style="left:150px">Copyright Varnel<span class="num">13</span></div>
</section>

<!-- 14 quote dark -->
<section class="slide">
  <div class="photo dark" style="inset:0" role="img" aria-label="Graduate holding a diploma"></div>
  <div class="abs" style="left:0;top:0;width:190px;height:219px;background:rgba(40,45,50,.85)"></div>
  <div class="abs" style="left:26px;top:40px;width:150px;color:#fff">
    <div style="font-size:20px;color:var(--cyan);line-height:16px">&ldquo;</div>
    <div style="font-size:10px;line-height:13px">Education is the most powerful weapon which you can use to change the world.</div>
    <div style="font-size:5px;margin-top:8px;color:#bbb">Ruth Calder</div>
  </div>
</section>

<!-- 15 list with photos -->
<section class="slide">
  <div class="ttl">Your Title Goes Here</div><div class="mark">VARNEL</div>
  <div class="abs" style="left:14px;top:40px;width:200px">
    <div class="row"><span class="ci"></span><div><div class="sh">Heading One</div><div class="p">Add a short line of body text here for this point.</div></div></div>
    <div class="row" style="margin-top:12px"><span class="ci"></span><div><div class="sh">Heading Two</div><div class="p">Add a short line of body text here for this point.</div></div></div>
    <div class="row" style="margin-top:12px"><span class="ci"></span><div><div class="sh">Heading Three</div><div class="p">Add a short line of body text here for this point.</div></div></div>
  </div>
  <div class="photo" style="left:250px;top:30px;width:128px;height:82px" role="img" aria-label="Student with headphones"></div>
  <div class="photo warm" style="left:250px;top:118px;width:128px;height:82px" role="img" aria-label="Students studying on a couch"></div>
  <div class="foot">Copyright Varnel<span class="num">15</span></div>
</section>

<!-- 16 portfolio -->
<section class="slide">
  <div class="ttl">Portfolio Area</div>
  <div class="abs" style="left:14px;top:34px;width:150px">
    <div class="sh ink">Heading Goes Here</div>
    <div class="p">Add a short line of body text here.</div>
    <div class="row" style="margin-top:8px"><span class="ci"></span><div><div class="sh">Your Text Here</div><div class="p">Short supporting line.</div></div></div>
    <div class="row" style="margin-top:6px"><span class="ci"></span><div><div class="sh">Your Text Here</div><div class="p">Short supporting line.</div></div></div>
    <div class="row" style="margin-top:6px"><span class="ci"></span><div><div class="sh">Your Text Here</div><div class="p">Short supporting line.</div></div></div>
  </div>
  <div class="photo warm" style="left:180px;top:0;width:212px;height:100px" role="img" aria-label="Teacher with a young student"></div>
  <div class="photo" style="left:180px;top:104px;width:104px;height:96px" role="img" aria-label="Children drawing"></div>
  <div class="photo cool" style="left:288px;top:104px;width:104px;height:96px" role="img" aria-label="Student reading"></div>
  <div class="foot">Copyright Varnel<span class="num">16</span></div>
</section>

<!-- 17 building -->
<section class="slide">
  <div class="ttl">Your Title Goes Here</div><div class="mark">VARNEL</div>
  <div class="abs" style="left:14px;top:40px;width:110px">
    <div class="sh ink">Heading Goes Here</div>
    <div class="p">Add a short paragraph of body text here to describe this point.</div>
  </div>
  <svg class="abs" style="left:130px;top:50px" width="110" height="130" viewBox="0 0 110 130">
    <g fill="none" stroke="#cfcfcf" stroke-width="1"><path d="M100 20 H60 V65 H100"/><path d="M60 65 V110 H100"/></g>
    <g fill="var(--cyan)"><circle cx="100" cy="20" r="3"/><circle cx="100" cy="65" r="3"/><circle cx="100" cy="110" r="3"/></g>
  </svg>
  <div class="abs" style="left:160px;top:55px;width:70px;text-align:right">
    <div class="sh">Your Text Here</div><div class="p" style="margin-bottom:30px">Short line.</div>
    <div class="sh">Your Text Here</div><div class="p" style="margin-bottom:30px">Short line.</div>
    <div class="sh">Your Text Here</div><div class="p">Short line.</div>
  </div>
  <div class="photo dark" style="left:245px;top:40px;width:140px;height:160px;background:linear-gradient(135deg,#5a3e32,#a28676)" role="img" aria-label="Campus building"></div>
  <div class="foot">Copyright Varnel<span class="num">17</span></div>
</section>

<!-- 18 services -->
<section class="slide">
  <div class="ttl">Our Services</div><div class="mark">VARNEL</div>
  <div class="photo warm" style="left:14px;top:34px;width:160px;height:110px" role="img" aria-label="Children learning at a table"></div>
  <div class="abs" style="left:14px;top:150px;width:160px"><div class="sh ink">Your Title Goes Here</div><div class="p">Add a short line of body text here.</div></div>
  <div class="abs" style="left:196px;top:40px;width:182px">
    <div class="row"><span class="ci"><svg viewBox="0 0 10 10"><path d="M2 5 L4 7 L8 3" stroke="#fff" stroke-width="1.5" fill="none"/></svg></span><div><div class="sh">Service Number One</div><div class="p">Add a short line of body text here.</div></div></div>
    <div class="row" style="margin-top:14px"><span class="ci"><svg viewBox="0 0 10 10"><path d="M2 5 L4 7 L8 3" stroke="#fff" stroke-width="1.5" fill="none"/></svg></span><div><div class="sh">Service Number Two</div><div class="p">Add a short line of body text here.</div></div></div>
    <div class="row" style="margin-top:14px"><span class="ci"><svg viewBox="0 0 10 10"><path d="M2 5 L4 7 L8 3" stroke="#fff" stroke-width="1.5" fill="none"/></svg></span><div><div class="sh">Service Number Three</div><div class="p">Add a short line of body text here.</div></div></div>
  </div>
  <div class="foot">Copyright Varnel<span class="num">18</span></div>
</section>

<!-- 19 collage -->
<section class="slide">
  <div class="photo cool" style="left:0;top:0;width:392px;height:219px;opacity:.35" role="img" aria-label="Faded classroom background"></div>
  <div class="photo" style="left:70px;top:14px;width:120px;height:70px" role="img" aria-label="Girl with a microscope"></div>
  <div class="abs cyanbg" style="left:0;top:14px;width:66px;height:70px;display:flex;align-items:center;padding-left:6px"><div class="brand" style="font-size:8px"><span class="disc" style="width:9px;height:9px"></span>VARNEL</div></div>
  <div class="photo warm" style="left:0;top:88px;width:92px;height:110px" role="img" aria-label="Children with books"></div>
  <div class="photo" style="left:96px;top:88px;width:94px;height:110px" role="img" aria-label="Student painting"></div>
  <div class="abs" style="left:214px;top:44px;width:160px"><div style="font-size:10px;line-height:12px">Your Title<br>Goes Here</div><div class="p" style="margin-top:6px">Add a short paragraph of body text here to describe this point for your audience.</div></div>
  <div class="foot">Copyright Varnel<span class="num">19</span></div>
</section>

<!-- 20 coffee break -->
<section class="slide cyanbg">
  <div class="mark light">VARNEL</div>
  <svg class="abs" style="left:184px;top:70px" width="24" height="24" viewBox="0 0 24 24"><path d="M4 8 H16 V16 a4 4 0 0 1 -4 4 H8 a4 4 0 0 1 -4 -4 Z M16 10 H19 a2 2 0 0 1 0 5 H16" fill="none" stroke="#fff" stroke-width="1.6"/><path d="M8 2 V5 M12 2 V5" stroke="#fff" stroke-width="1.4"/></svg>
  <div class="abs" style="left:0;right:0;top:100px;text-align:center;color:#fff;font-size:12px;font-weight:600;letter-spacing:1px">COFFEE BREAK</div>
  <div class="abs" style="left:0;right:0;top:116px;text-align:center;color:#fff;font-size:5px">Back in 15 minutes</div>
</section>

<!-- 21 we are -->
<section class="slide">
  <div class="ttl">Your Title Goes Here</div><div class="mark">VARNEL</div>
  <div class="abs" style="left:14px;top:34px;width:170px">
    <div class="hl">We are <b>Varnel</b><br>Choose Better. Learn Better.</div>
    <div class="p" style="margin-top:6px">Add a short paragraph of body text here to describe this point for your audience.</div>
    <div class="p" style="margin-top:6px">Add a second paragraph of body text here to expand on the point above.</div>
  </div>
  <div class="photo" style="left:196px;top:34px;width:88px;height:110px" role="img" aria-label="Student in a science lab"></div>
  <div class="photo warm" style="left:290px;top:34px;width:88px;height:110px" role="img" aria-label="Students with a teacher"></div>
  <div class="foot">Copyright Varnel<span class="num">21</span></div>
</section>

<!-- 22 two column -->
<section class="slide">
  <div class="ttl">Two Column Description</div><div class="mark">VARNEL</div>
  <div class="abs" style="left:14px;top:36px"><div class="hl">We are <b>Varnel</b><br>Choose Better. Learn Better.</div></div>
  <div class="abs" style="left:14px;top:66px;width:364px;display:grid;grid-template-columns:1fr 1fr;gap:20px">
    <div><div class="p">Add a short paragraph of body text here to describe this point for your audience in plain words.</div><div class="p" style="margin-top:6px">Add a second paragraph here to expand on the point above with detail.</div></div>
    <div><div class="p">Add a short paragraph of body text here to describe this point for your audience in plain words.</div><div class="p" style="margin-top:6px">Add a second paragraph here to expand on the point above with detail.</div></div>
  </div>
  <div class="foot">Copyright Varnel<span class="num">22</span></div>
</section>

<!-- 23 numbered -->
<section class="slide">
  <div class="ttl">Your Title Goes Here</div><div class="mark">VARNEL</div>
  <div class="abs" style="left:14px;top:36px;width:160px">
    <div class="sh ink">Heading Goes Here</div><div class="p" style="margin-bottom:8px">Add a short line of body text here.</div>
    <div class="row"><span class="ci" style="background:#bdbdbd"></span><div><div class="sh">Service Number One</div><div class="p">Short supporting line.</div></div></div>
    <div class="row" style="margin-top:8px"><span class="ci" style="background:#bdbdbd"></span><div><div class="sh">Service Number Two</div><div class="p">Short supporting line.</div></div></div>
    <div class="row" style="margin-top:8px"><span class="ci" style="background:#bdbdbd"></span><div><div class="sh">Service Number Three</div><div class="p">Short supporting line.</div></div></div>
  </div>
  <div class="abs" style="left:196px;top:44px;width:182px">
    <div style="display:flex;margin-bottom:8px"><span class="sq" style="width:22px;height:28px;font-size:11px;background:var(--dark)">1</span><div style="flex:1;background:#f2f2f2;padding:4px"><div class="sh ink">Your Text Here</div><div class="p">Short supporting line.</div></div></div>
    <div style="display:flex;margin-bottom:8px"><span class="sq" style="width:22px;height:28px;font-size:11px;background:var(--dark)">2</span><div style="flex:1;background:#f2f2f2;padding:4px"><div class="sh ink">Your Text Here</div><div class="p">Short supporting line.</div></div></div>
    <div style="display:flex"><span class="sq" style="width:22px;height:28px;font-size:11px">3</span><div style="flex:1;background:#f2f2f2;padding:4px"><div class="sh ink">Your Text Here</div><div class="p">Short supporting line.</div></div></div>
  </div>
  <div class="foot">Copyright Varnel<span class="num">23</span></div>
</section>

<!-- 24 three column -->
<section class="slide">
  <div class="ttl">Three Column Description</div><div class="mark">VARNEL</div>
  <div class="abs" style="left:14px;top:36px"><div class="hl">We are <b>Varnel</b><br>Choose Better. Learn Better.</div></div>
  <div class="abs" style="left:14px;top:66px;width:364px;display:grid;grid-template-columns:repeat(3,1fr);gap:14px">
    <div class="p">Add a short paragraph of body text here to describe this point for your audience in plain words and clear terms.</div>
    <div class="p">Add a short paragraph of body text here to describe this point for your audience in plain words and clear terms.</div>
    <div class="p">Add a short paragraph of body text here to describe this point for your audience in plain words and clear terms.</div>
  </div>
  <div class="foot">Copyright Varnel<span class="num">24</span></div>
</section>

<!-- 25 photo logo with checks -->
<section class="slide">
  <div class="photo" style="left:0;top:0;width:170px;height:120px" role="img" aria-label="Student with backpack"></div>
  <div class="abs cyanbg" style="left:0;top:120px;width:170px;height:90px;display:flex;align-items:center;padding-left:16px"><div class="brand" style="font-size:14px"><span class="disc" style="width:16px;height:16px"></span>VARNEL</div></div>
  <div class="abs" style="left:190px;top:40px;width:186px">
    <div style="font-size:10px">Your Title Goes Here</div>
    <div class="p" style="margin:4px 0 10px">Add a short line of body text here.</div>
    <div class="row"><span class="sq"></span><div><div class="sh">Your Text Goes Here</div><div class="p">Short supporting line here.</div></div></div>
    <div class="row" style="margin-top:10px"><span class="sq"></span><div><div class="sh">Your Text Goes Here</div><div class="p">Short supporting line here.</div></div></div>
  </div>
  <div class="foot">Copyright Varnel<span class="num">25</span></div>
</section>

<!-- 26 differences -->
<section class="slide">
  <div class="ttl">Our Differences</div><div class="mark">VARNEL</div>
  <div class="abs cyanbg" style="left:14px;top:50px;width:364px;height:110px"></div>
  <div class="abs" style="left:24px;top:62px;width:190px">
    <div class="row"><span class="ci" style="background:#fff"></span><div class="p w">Add a short line of body text here for this point.</div></div>
    <div class="row" style="margin-top:10px"><span class="ci" style="background:#fff"></span><div class="p w">Add a short line of body text here for this point.</div></div>
    <div class="row" style="margin-top:10px"><span class="ci" style="background:#fff"></span><div class="p w">Add a short line of body text here for this point.</div></div>
  </div>
  <div class="photo dark" style="left:226px;top:60px;width:142px;height:90px" role="img" aria-label="Students in a computer lab"></div>
  <div class="foot">Copyright Varnel<span class="num">26</span></div>
</section>

<!-- 27 woman cyan panel -->
<section class="slide">
  <div class="photo warm" style="left:0;top:0;width:392px;height:219px" role="img" aria-label="Smiling student holding books"></div>
  <div class="abs cyanbg" style="left:246px;top:0;width:146px;height:210px;padding:18px 12px">
    <div class="brand" style="font-size:11px"><span class="disc" style="width:12px;height:12px"></span>VARNEL</div>
    <div style="color:#fff;font-size:10px;margin-top:60px">Your Title Goes Here</div>
    <div class="p w" style="margin-top:4px">Add a short line of body text here for this point.</div>
  </div>
  <div class="foot">Copyright Varnel<span class="num">27</span></div>
</section>

<!-- 28 multiple column -->
<section class="slide">
  <div class="ttl">Multiple Column Area</div><div class="mark">VARNEL</div>
  <div class="abs" style="left:14px;top:40px;width:364px;display:grid;grid-template-columns:repeat(5,1fr);gap:8px;text-align:center">
    <div><span class="ci"></span><div class="sh ink">Your Text</div><div class="p">Short line.</div></div>
    <div><span class="ci"></span><div class="sh ink">Your Text</div><div class="p">Short line.</div></div>
    <div><span class="ci"></span><div class="sh ink">Your Text</div><div class="p">Short line.</div></div>
    <div><span class="ci"></span><div class="sh ink">Your Text</div><div class="p">Short line.</div></div>
    <div><span class="ci"></span><div class="sh ink">Your Text</div><div class="p">Short line.</div></div>
  </div>
  <div class="abs" style="left:14px;top:100px;width:364px;border-top:1px solid var(--line);padding-top:8px;display:grid;grid-template-columns:1fr 1fr;gap:20px">
    <div><div class="sh ink">Heading Goes Here</div><div class="p">Add a short paragraph of body text here to describe this point.</div></div>
    <div><div class="sh ink">Heading Goes Here</div><div class="p">Add a short paragraph of body text here to describe this point.</div></div>
  </div>
  <div class="foot">Copyright Varnel<span class="num">28</span></div>
</section>

<!-- 29 cyan overlay title -->
<section class="slide">
  <div class="photo tint" style="inset:0" role="img" aria-label="Students in class under a cyan tint"></div>
  <div class="mark light">VARNEL</div>
  <div class="abs" style="left:40px;top:130px;color:#fff"><div style="font-size:6px">Some Text</div><div style="font-size:12px">Your Subtitle Here</div></div>
</section>

<!-- 30 paragraph three bullet -->
<section class="slide">
  <div class="ttl">Paragraph with Three Bullet</div><div class="mark">VARNEL</div>
  <div class="abs" style="left:14px;top:36px;width:150px">
    <div class="hl">We are <b>Varnel</b><br>Choose Better. Learn Better.</div>
    <div class="p" style="margin-top:6px">Add a short paragraph of body text here to describe this point for your audience.</div>
    <div class="p" style="margin-top:6px">Add a second paragraph of body text here to expand on the point above.</div>
  </div>
  <div class="abs" style="left:180px;top:50px;width:200px;display:grid;grid-template-columns:repeat(3,1fr);gap:8px;text-align:center">
    <div><span class="ci" style="width:22px;height:22px;background:#fff;border:1px solid var(--cyan)"></span><div class="sh ink">Your Text</div><div class="p">Add a short line here.</div></div>
    <div><span class="ci" style="width:22px;height:22px;background:#fff;border:1px solid var(--cyan)"></span><div class="sh ink">Your Text</div><div class="p">Add a short line here.</div></div>
    <div><span class="ci" style="width:22px;height:22px;background:#fff;border:1px solid var(--cyan)"></span><div class="sh ink">Your Text</div><div class="p">Add a short line here.</div></div>
  </div>
  <div class="foot">Copyright Varnel<span class="num">30</span></div>
</section>

<!-- 31 title photo -->
<section class="slide">
  <div class="mark" style="left:14px;right:auto">VARNEL</div>
  <div class="abs" style="left:14px;top:40px;width:100px">
    <div style="font-size:11px;line-height:13px">Your Title<br>Goes Here</div>
    <div class="p" style="margin-top:6px">Add a short paragraph of body text here for this point.</div>
    <div class="p" style="margin-top:4px">&#8226; Your text here<br>&#8226; Your text here<br>&#8226; Your text here</div>
  </div>
  <div class="photo warm" style="left:124px;top:0;width:268px;height:210px" role="img" aria-label="Group of students in a classroom"></div>
  <div class="foot">Copyright Varnel<span class="num">31</span></div>
</section>

<!-- 32 rocket chalkboard -->
<section class="slide">
  <div class="ttl">Your Title</div><div class="mark">VARNEL</div>
  <div class="abs" style="left:14px;top:34px;width:80px"><div class="sh ink">Heading Goes Here</div><div class="p">Add a short paragraph of body text here.</div></div>
  <div class="photo dark" style="left:100px;top:0;width:160px;height:210px" role="img" aria-label="Child in front of a chalkboard with a drawn rocket"></div>
  <div class="abs" style="left:270px;top:40px;width:112px">
    <div class="row"><span class="ci"></span><div><div class="sh">Your Text Here</div><div class="p">Short line.</div></div></div>
    <div class="row" style="margin-top:10px"><span class="ci"></span><div><div class="sh">Your Text Here</div><div class="p">Short line.</div></div></div>
    <div class="row" style="margin-top:10px"><span class="ci"></span><div><div class="sh">Your Text Here</div><div class="p">Short line.</div></div></div>
    <div class="row" style="margin-top:10px"><span class="ci"></span><div><div class="sh">Your Text Here</div><div class="p">Short line.</div></div></div>
  </div>
  <div class="foot">Copyright Varnel<span class="num">32</span></div>
</section>

<!-- 33 chalkboard -->
<section class="slide">
  <div class="ttl">Your Title Goes Here</div><div class="mark">VARNEL</div>
  <div class="abs" style="left:14px;top:36px;width:140px">
    <div class="sh ink">Heading Goes Here</div>
    <div class="p">Add a short paragraph of body text here to describe this point for your audience.</div>
    <div class="p" style="margin-top:6px">Add a second paragraph of body text here to expand on the point.</div>
  </div>
  <div class="photo dark" style="left:166px;top:30px;width:212px;height:170px" role="img" aria-label="Chalkboard with drawn ideas and a student"></div>
  <div class="foot">Copyright Varnel<span class="num">33</span></div>
</section>

<!-- 34 four bullets paragraph -->
<section class="slide">
  <div class="ttl">Four Bullets with Paragraph</div><div class="mark">VARNEL</div>
  <div class="abs" style="left:14px;top:40px;width:190px;display:grid;grid-template-columns:1fr 1fr;gap:14px 10px">
    <div class="row"><span class="ci"></span><div><div class="sh">Your Text</div><div class="p">Short line here.</div></div></div>
    <div class="row"><span class="ci"></span><div><div class="sh">Your Text</div><div class="p">Short line here.</div></div></div>
    <div class="row"><span class="ci"></span><div><div class="sh">Your Text</div><div class="p">Short line here.</div></div></div>
    <div class="row"><span class="ci"></span><div><div class="sh">Your Text</div><div class="p">Short line here.</div></div></div>
  </div>
  <div class="abs" style="left:220px;top:40px;width:158px">
    <div style="font-size:9px">Your Title Goes Here</div>
    <div class="p" style="margin-top:5px">Add a short paragraph of body text here to describe this point for your audience in plain words.</div>
  </div>
  <div class="foot">Copyright Varnel<span class="num">34</span></div>
</section>

<!-- 35 cyan photo top list -->
<section class="slide">
  <div class="photo tint" style="left:0;top:0;width:392px;height:100px" role="img" aria-label="Students under a cyan tint"></div>
  <div class="mark light" style="left:14px;right:auto">VARNEL</div>
  <div class="abs" style="left:150px;top:36px;color:#fff;font-size:11px">Your Title Goes Here</div>
  <div class="photo" style="left:14px;top:80px;width:110px;height:110px" role="img" aria-label="Group of children smiling"></div>
  <div class="abs" style="left:140px;top:112px;width:240px;display:grid;grid-template-columns:1fr 1fr;gap:12px">
    <div class="row"><span class="ci"></span><div><div class="sh">Your Text Here</div><div class="p">Short line.</div></div></div>
    <div class="row"><span class="ci"></span><div><div class="sh">Your Text Here</div><div class="p">Short line.</div></div></div>
    <div class="row"><span class="ci"></span><div><div class="sh">Your Text Here</div><div class="p">Short line.</div></div></div>
    <div class="row"><span class="ci"></span><div><div class="sh">Your Text Here</div><div class="p">Short line.</div></div></div>
  </div>
  <div class="foot">Copyright Varnel<span class="num">35</span></div>
</section>

<!-- 36 text & bullet -->
<section class="slide">
  <div class="ttl">Text &amp; Bullet Area</div><div class="mark">VARNEL</div>
  <div class="abs" style="left:14px;top:36px;width:120px">
    <div class="sh ink">Heading Goes Here</div><div class="p">Add a short paragraph of body text here for this point.</div>
    <div class="sh ink" style="margin-top:8px">Heading Goes Here</div><div class="p">Add a short paragraph of body text here for this point.</div>
  </div>
  <div class="abs" style="left:150px;top:36px;width:228px;display:grid;grid-template-columns:1fr 1fr;gap:12px 10px">
    <div class="row"><span class="ci"></span><div><div class="sh">Your Text Here</div><div class="p">Short line.</div></div></div>
    <div class="row"><span class="ci"></span><div><div class="sh">Your Text Here</div><div class="p">Short line.</div></div></div>
    <div class="row"><span class="ci"></span><div><div class="sh">Your Text Here</div><div class="p">Short line.</div></div></div>
    <div class="row"><span class="ci"></span><div><div class="sh">Your Text Here</div><div class="p">Short line.</div></div></div>
    <div class="row"><span class="ci"></span><div><div class="sh">Your Text Here</div><div class="p">Short line.</div></div></div>
    <div class="row"><span class="ci"></span><div><div class="sh">Your Text Here</div><div class="p">Short line.</div></div></div>
    <div class="row"><span class="ci"></span><div><div class="sh">Your Text Here</div><div class="p">Short line.</div></div></div>
    <div class="row"><span class="ci"></span><div><div class="sh">Your Text Here</div><div class="p">Short line.</div></div></div>
  </div>
  <div class="foot">Copyright Varnel<span class="num">36</span></div>
</section>

<!-- 37 video -->
<section class="slide">
  <div class="abs" style="left:14px;top:40px;width:110px">
    <div style="font-size:10px;line-height:12px">Your Video Tittle<br>Goes Here</div>
    <div class="p" style="margin-top:6px">Add a short paragraph of body text here to describe this video.</div>
  </div>
  <div class="abs" style="left:140px;top:40px;width:230px;height:136px;background:#2d2d2d;border-radius:4px;padding:6px">
    <div class="photo warm" style="position:relative;width:100%;height:100%" role="img" aria-label="Video still of a teacher"></div>
  </div>
  <svg class="abs" style="left:241px;top:93px" width="28" height="28" viewBox="0 0 28 28"><circle cx="14" cy="14" r="13" fill="var(--cyan)"/><path d="M11 8 L20 14 L11 20 Z" fill="#fff"/></svg>
  <div class="abs" style="left:240px;top:176px;width:30px;height:14px;background:#cfcfcf"></div>
  <div class="abs" style="left:220px;top:190px;width:70px;height:3px;background:#cfcfcf;border-radius:2px"></div>
  <div class="foot">Copyright Varnel<span class="num">37</span></div>
</section>

<!-- 38 pictures with bullets -->
<section class="slide">
  <div class="ttl">Pictures with Bullets</div><div class="mark">VARNEL</div>
  <div class="photo" style="left:14px;top:34px;width:175px;height:80px" role="img" aria-label="Students at a lab bench"></div>
  <div class="photo warm" style="left:203px;top:34px;width:175px;height:80px" role="img" aria-label="Children learning outdoors"></div>
  <div class="abs" style="left:14px;top:122px;width:175px"><div class="sh ink">Heading Goes Here</div><div class="p">&#8226; Your text here &nbsp; &#8226; Your text here<br>&#8226; Your text here &nbsp; &#8226; Your text here</div></div>
  <div class="abs" style="left:203px;top:122px;width:175px"><div class="sh ink">Heading Goes Here</div><div class="p">&#8226; Your text here &nbsp; &#8226; Your text here<br>&#8226; Your text here &nbsp; &#8226; Your text here</div></div>
  <div class="foot">Copyright Varnel<span class="num">38</span></div>
</section>

<!-- 39 video gallery -->
<section class="slide">
  <div class="ttl">Our Video Gallery</div><div class="mark">VARNEL</div>
  <div class="photo" style="left:14px;top:34px;width:70px;height:48px" role="img" aria-label="Video thumbnail of a classroom"></div>
  <div class="photo warm" style="left:90px;top:34px;width:70px;height:48px" role="img" aria-label="Video thumbnail of students"></div>
  <div class="photo" style="left:166px;top:34px;width:70px;height:48px" role="img" aria-label="Video thumbnail of a teacher"></div>
  <div class="abs" style="left:14px;top:90px;width:222px"><div class="sh ink">Heading Goes Here</div><div class="p">Add a short paragraph of body text here to describe this video series.</div></div>
  <div class="abs" style="left:250px;top:40px;width:130px;height:100px;background:#2d2d2d;border-radius:6px;padding:6px">
    <div class="photo warm" style="position:relative;width:100%;height:100%" role="img" aria-label="Video still on a tablet"></div>
  </div>
  <svg class="abs" style="left:305px;top:80px" width="20" height="20" viewBox="0 0 28 28"><circle cx="14" cy="14" r="13" fill="var(--cyan)"/><path d="M11 8 L20 14 L11 20 Z" fill="#fff"/></svg>
  <div class="foot">Copyright Varnel<span class="num">39</span></div>
</section>

<!-- 40 key points -->
<section class="slide">
  <div class="ttl">Key Points Area</div><div class="mark">VARNEL</div>
  <svg class="abs" style="left:30px;top:52px" width="180" height="40" viewBox="0 0 180 40">
    <g fill="#8f8f8f"><circle cx="20" cy="20" r="18"/><circle cx="62" cy="20" r="18" fill="#b5b5b5"/><circle cx="104" cy="20" r="18" fill="var(--cyan)"/><circle cx="146" cy="20" r="18" fill="#b5b5b5"/></g>
    <g fill="#fff"><path d="M36 14 L42 20 L36 26 Z"/><path d="M78 14 L84 20 L78 26 Z"/><path d="M120 14 L126 20 L120 26 Z"/></g>
  </svg>
  <div class="abs" style="left:14px;top:110px;width:364px;display:grid;grid-template-columns:repeat(4,1fr);gap:10px">
    <div><div class="sh ink">Your Text</div><div class="p">Add a short line here.</div></div>
    <div><div class="sh ink">Your Text</div><div class="p">Add a short line here.</div></div>
    <div><div class="sh">Your Text</div><div class="p">Add a short line here.</div></div>
    <div><div class="sh ink">Your Text</div><div class="p">Add a short line here.</div></div>
  </div>
  <div class="foot">Copyright Varnel<span class="num">40</span></div>
</section>

<!-- 41 four column circles -->
<section class="slide">
  <div class="ttl">Four Column Area</div><div class="mark">VARNEL</div>
  <div class="abs" style="left:14px;top:44px;width:364px;display:grid;grid-template-columns:repeat(4,1fr);gap:10px;text-align:center">
    <div><span class="ci" style="width:34px;height:34px;background:#fff;border:2px solid var(--cyan)"></span><div class="sh ink" style="margin-top:6px">Your Text</div><div class="p">Add a short line of body text here.</div></div>
    <div><span class="ci" style="width:34px;height:34px;background:#fff;border:2px solid var(--cyan)"></span><div class="sh ink" style="margin-top:6px">Your Text</div><div class="p">Add a short line of body text here.</div></div>
    <div><span class="ci" style="width:34px;height:34px;background:#fff;border:2px solid var(--cyan)"></span><div class="sh ink" style="margin-top:6px">Your Text</div><div class="p">Add a short line of body text here.</div></div>
    <div><span class="ci" style="width:34px;height:34px;background:#fff;border:2px solid var(--cyan)"></span><div class="sh ink" style="margin-top:6px">Your Text</div><div class="p">Add a short line of body text here.</div></div>
  </div>
  <div class="foot">Copyright Varnel<span class="num">41</span></div>
</section>

<!-- 42 four column boxes -->
<section class="slide">
  <div class="ttl">Four Column Area</div><div class="mark">VARNEL</div>
  <div class="abs" style="left:14px;top:50px;width:364px;display:grid;grid-template-columns:repeat(4,1fr);gap:6px;text-align:center">
    <div style="background:#f1f1f1;height:80px;padding-top:12px"><span class="ci" style="background:#9a9a9a"></span><div class="sh ink">Your Text</div><div class="p">Short line here.</div></div>
    <div style="background:var(--cyan);height:92px;margin-top:-6px;padding-top:18px"><span class="ci" style="background:#fff"></span><div class="sh" style="color:#fff">Your Text</div><div class="p w">Short line here.</div></div>
    <div style="background:#f1f1f1;height:80px;padding-top:12px"><span class="ci" style="background:#9a9a9a"></span><div class="sh ink">Your Text</div><div class="p">Short line here.</div></div>
    <div style="background:#f1f1f1;height:80px;padding-top:12px"><span class="ci" style="background:#9a9a9a"></span><div class="sh ink">Your Text</div><div class="p">Short line here.</div></div>
  </div>
  <div class="abs p" style="left:14px;top:150px;width:364px;text-align:center">Add a short line of body text here to close this section.</div>
  <div class="foot">Copyright Varnel<span class="num">42</span></div>
</section>

<!-- 43 workflow -->
<section class="slide">
  <div class="ttl">Workflow Area</div><div class="mark">VARNEL</div>
  <svg class="abs" style="left:20px;top:60px" width="352" height="80" viewBox="0 0 352 80">
    <path d="M10 40 C50 -5 90 -5 130 40 S210 85 250 40 S320 0 342 20" fill="none" stroke="var(--cyan)" stroke-width="12"/>
    <path d="M10 40 C50 -5 90 -5 130 40" fill="none" stroke="#9a9a9a" stroke-width="12"/>
  </svg>
  <div class="abs" style="left:40px;top:44px;text-align:center"><div class="sh ink">Step 1</div></div>
  <div class="abs" style="left:140px;top:100px;text-align:center"><div class="sh ink">Step 2</div></div>
  <div class="abs" style="left:240px;top:44px;text-align:center"><div class="sh ink">Step 3</div></div>
  <div class="abs" style="left:14px;top:150px;width:364px;display:grid;grid-template-columns:repeat(3,1fr);gap:10px">
    <div class="p">Add a short line of body text here.</div>
    <div class="p">Add a short line of body text here.</div>
    <div class="p">Add a short line of body text here.</div>
  </div>
  <div class="foot">Copyright Varnel<span class="num">43</span></div>
</section>

<!-- 44 global -->
<section class="slide">
  <div class="ttl">Global Experience</div><div class="mark">VARNEL</div>
  <div class="photo" style="left:40px;top:34px;width:320px;height:120px;background:linear-gradient(135deg,#d4d9dc,#eef1f2)" role="img" aria-label="World map with office locations"></div>
  <div class="abs" style="left:14px;top:160px;width:200px"><div class="sh">Heading Goes Here</div><div class="p">Add a short line of body text here for this section.</div></div>
  <div class="foot">Copyright Varnel<span class="num">44</span></div>
</section>

<!-- 45 timeline -->
<section class="slide">
  <div class="ttl">Timeline</div><div class="mark">VARNEL</div>
  <div class="abs" style="left:20px;top:90px;width:352px;height:2px;background:var(--line)"></div>
  <div class="abs" style="left:24px;top:50px;width:344px;display:flex;justify-content:space-between">
    <span class="ci" style="width:30px;height:30px;background:#9a9a9a;color:#fff;font-size:6px;margin-top:26px">2012</span>
    <span class="ci" style="width:30px;height:30px;background:#b5b5b5;color:#fff;font-size:6px">2013</span>
    <span class="ci" style="width:30px;height:30px;background:#9a9a9a;color:#fff;font-size:6px;margin-top:26px">2014</span>
    <span class="ci" style="width:30px;height:30px;background:#b5b5b5;color:#fff;font-size:6px">2015</span>
    <span class="ci" style="width:30px;height:30px;background:var(--cyan);color:#fff;font-size:6px;margin-top:26px">2016</span>
  </div>
  <div class="abs" style="left:280px;top:120px;width:100px"><div class="sh">Your Text Here</div><div class="p">Add a short line here.</div></div>
  <div class="abs" style="left:20px;top:120px;width:100px"><div class="sh ink">Your Text Here</div><div class="p">Add a short line here.</div></div>
  <div class="foot">Copyright Varnel<span class="num">45</span></div>
</section>

<!-- 46 bar chart -->
<section class="slide">
  <div class="ttl">Bullet &amp; Chart Area</div><div class="mark">VARNEL</div>
  <svg class="abs" style="left:14px;top:40px" width="180" height="150" viewBox="0 0 180 150">
    <g font-size="5" fill="#8d8d8d" font-family="Open Sans, sans-serif"><text x="0" y="14">Category 1</text><text x="0" y="44">Category 2</text><text x="0" y="74">Category 3</text><text x="0" y="104">Category 4</text><text x="0" y="134">Category 5</text></g>
    <g fill="var(--cyan)"><rect x="34" y="6" width="100" height="5"/><rect x="34" y="36" width="70" height="5"/><rect x="34" y="66" width="120" height="5"/><rect x="34" y="96" width="60" height="5"/><rect x="34" y="126" width="90" height="5"/></g>
    <g fill="#5e6468"><rect x="34" y="13" width="80" height="5"/><rect x="34" y="43" width="110" height="5"/><rect x="34" y="73" width="50" height="5"/><rect x="34" y="103" width="95" height="5"/><rect x="34" y="133" width="65" height="5"/></g>
  </svg>
  <div class="abs" style="left:214px;top:40px;width:166px">
    <div class="row"><span class="ci"></span><div><div class="sh ink">Category One</div><div class="p">Short line.</div></div></div>
    <div class="row" style="margin-top:8px"><span class="ci"></span><div><div class="sh ink">Category Two</div><div class="p">Short line.</div></div></div>
    <div class="row" style="margin-top:8px"><span class="ci"></span><div><div class="sh ink">Category Three</div><div class="p">Short line.</div></div></div>
    <div class="row" style="margin-top:8px"><span class="ci"></span><div><div class="sh ink">Category Four</div><div class="p">Short line.</div></div></div>
  </div>
  <div class="foot">Copyright Varnel<span class="num">46</span></div>
</section>

<!-- 47 table -->
<section class="slide">
  <div class="ttl">Table Area</div><div class="mark">VARNEL</div>
  <table class="abs" style="left:60px;top:40px;width:272px;font-size:5px;color:var(--muted)">
    <thead><tr style="background:var(--dark);color:#fff;height:14px"><th style="text-align:left;padding-left:6px">Description</th><th>Column A</th><th style="background:var(--cyan)">Column B</th></tr></thead>
    <tbody>
      <tr style="height:16px;border-bottom:1px solid var(--line)"><td style="padding-left:6px">Description 1</td><td style="text-align:center">&#10003;</td><td style="text-align:center">&#10003;</td></tr>
      <tr style="height:16px;border-bottom:1px solid var(--line);background:#f7f7f7"><td style="padding-left:6px">Description 2</td><td style="text-align:center">&#10003;</td><td style="text-align:center">&#10003;</td></tr>
      <tr style="height:16px;border-bottom:1px solid var(--line)"><td style="padding-left:6px">Description 3</td><td style="text-align:center">&ndash;</td><td style="text-align:center">&#10003;</td></tr>
      <tr style="height:16px;border-bottom:1px solid var(--line);background:#f7f7f7"><td style="padding-left:6px">Description 4</td><td style="text-align:center">&#10003;</td><td style="text-align:center">&#10003;</td></tr>
      <tr style="height:16px;border-bottom:1px solid var(--line)"><td style="padding-left:6px">Description 5</td><td style="text-align:center">&ndash;</td><td style="text-align:center">&#10003;</td></tr>
      <tr style="height:16px"><td style="padding-left:6px">Description 6</td><td style="text-align:center">&#10003;</td><td style="text-align:center">&#10003;</td></tr>
    </tbody>
  </table>
  <div class="foot">Copyright Varnel<span class="num">47</span></div>
</section>

<!-- 48 donut -->
<section class="slide">
  <div class="ttl">Bullet &amp; Chart Area</div><div class="mark">VARNEL</div>
  <div class="abs" style="left:14px;top:40px;width:160px">
    <div class="row"><span class="ci"></span><div><div class="sh ink">Your Text Here</div><div class="p">Short line.</div></div></div>
    <div class="row" style="margin-top:10px"><span class="ci"></span><div><div class="sh ink">Your Text Here</div><div class="p">Short line.</div></div></div>
    <div class="row" style="margin-top:10px"><span class="ci"></span><div><div class="sh ink">Your Text Here</div><div class="p">Short line.</div></div></div>
    <div class="row" style="margin-top:10px"><span class="ci"></span><div><div class="sh ink">Your Text Here</div><div class="p">Short line.</div></div></div>
  </div>
  <svg class="abs" style="left:230px;top:50px" width="110" height="110" viewBox="0 0 110 110">
    <g transform="rotate(-90 55 55)" fill="none" stroke-width="14">
      <circle cx="55" cy="55" r="36" stroke="var(--cyan)" stroke-dasharray="33.9 192.3"/>
      <circle cx="55" cy="55" r="36" stroke="#b5b5b5" stroke-dasharray="0 33.9 56.5 135.8"/>
      <circle cx="55" cy="55" r="36" stroke="#5e6468" stroke-dasharray="0 90.4 135.7 0"/>
    </g>
  </svg>
  <div class="abs" style="left:232px;top:52px;font-size:8px;color:var(--cyan)">15%</div>
  <div class="abs" style="left:214px;top:140px;font-size:8px;color:var(--grey)">25%</div>
  <div class="abs" style="left:346px;top:100px;font-size:8px;color:var(--ink)">60%</div>
  <div class="foot">Copyright Varnel<span class="num">48</span></div>
</section>

<!-- 49 pricing -->
<section class="slide">
  <div class="ttl">Pricing Structure</div>
  <table class="abs" style="left:14px;top:32px;width:300px;font-size:5px;color:var(--muted)">
    <thead><tr style="height:14px"><th style="text-align:left;color:var(--cyan);font-size:6px">Choose Your Plan</th><th style="background:#e6e6e6">BASIC</th><th style="background:#e6e6e6">SUPER</th><th style="background:#e6e6e6">PREMIUM</th></tr></thead>
    <tbody>
      <tr style="height:14px;border-bottom:1px solid var(--line)"><td><span style="color:var(--cyan)">&#9632;</span> Description One</td><td style="text-align:center">&#10003;</td><td style="text-align:center">&#10003;</td><td style="text-align:center">&#10003;</td></tr>
      <tr style="height:14px;border-bottom:1px solid var(--line)"><td><span style="color:var(--cyan)">&#9632;</span> Description Two</td><td style="text-align:center">&ndash;</td><td style="text-align:center">&#10003;</td><td style="text-align:center">&#10003;</td></tr>
      <tr style="height:14px;border-bottom:1px solid var(--line)"><td><span style="color:var(--cyan)">&#9632;</span> Description Three</td><td style="text-align:center">&ndash;</td><td style="text-align:center">&#10003;</td><td style="text-align:center">&#10003;</td></tr>
      <tr style="height:14px;border-bottom:1px solid var(--line)"><td><span style="color:var(--cyan)">&#9632;</span> Description Four</td><td style="text-align:center">&ndash;</td><td style="text-align:center">&ndash;</td><td style="text-align:center">&#10003;</td></tr>
      <tr style="height:14px;border-bottom:1px solid var(--line)"><td><span style="color:var(--cyan)">&#9632;</span> Description Five</td><td style="text-align:center">&ndash;</td><td style="text-align:center">&ndash;</td><td style="text-align:center">&#10003;</td></tr>
      <tr style="height:16px"><td style="background:var(--cyan);color:#fff;padding-left:4px">Price</td><td style="background:#9a9a9a;color:#fff;text-align:center">$10</td><td style="background:#7e7e7e;color:#fff;text-align:center">$20</td><td style="background:#5e6468;color:#fff;text-align:center">$30</td></tr>
    </tbody>
  </table>
  <div class="abs p" style="left:14px;top:150px">Add a short note about the plans here.</div>
  <div class="foot">Copyright Varnel<span class="num">49</span></div>
</section>

<!-- 50 team -->
<section class="slide">
  <div class="photo dark" style="left:0;top:0;width:140px;height:219px;background:linear-gradient(135deg,#8a8f93,#c9cdd0)" role="img" aria-label="City buildings in grey tones"></div>
  <div class="abs" style="left:14px;top:186px;color:#fff;font-size:9px">Meet Our Team</div>
  <div class="abs" style="left:160px;top:14px;width:220px;display:grid;grid-template-columns:1fr 1fr;gap:14px 10px">
    <div class="row" style="grid-column:1/3;justify-content:center"><span class="ci" style="width:28px;height:28px;background:#cfd8dd;border:2px solid var(--cyan)"></span><div><div class="sh ink">Nora Vale</div><div class="p">Founder &amp; CEO</div></div></div>
    <div class="row"><span class="ci" style="width:24px;height:24px;background:#cfd8dd"></span><div><div class="sh ink">Alex Reed</div><div class="p">Job Title</div></div></div>
    <div class="row"><span class="ci" style="width:24px;height:24px;background:#cfd8dd"></span><div><div class="sh ink">Mia Lane</div><div class="p">Job Title</div></div></div>
    <div class="row"><span class="ci" style="width:24px;height:24px;background:#cfd8dd"></span><div><div class="sh ink">Sam Cole</div><div class="p">Job Title</div></div></div>
    <div class="row"><span class="ci" style="width:24px;height:24px;background:#cfd8dd"></span><div><div class="sh ink">Lea Ford</div><div class="p">Job Title</div></div></div>
  </div>
</section>

<!-- 51 thank you -->
<section class="slide">
  <div class="photo" style="left:0;top:0;width:392px;height:219px;background:linear-gradient(135deg,#9aa3a8,#d4d9dc)" role="img" aria-label="Student at a desk in grey tones"></div>
  <div class="abs cyanbg" style="left:0;top:0;width:210px;height:219px;opacity:.92"></div>
  <div class="abs" style="left:20px;top:20px"><div class="brand" style="font-size:14px"><span class="disc" style="width:16px;height:16px"></span>VARNEL</div></div>
  <div class="abs" style="left:20px;top:60px;color:#fff;font-size:7px;font-weight:600">Our Contact</div>
  <div class="abs p w" style="left:20px;top:74px;line-height:10px">&#9679; 12 Orchard Lane, Brookfield<br>&#9679; +1 555 014 2290<br>&#9679; hello@varnel-learn.com<br>&#9679; www.varnel-learn.com</div>
  <div class="abs" style="left:236px;top:80px;color:#fff;font-size:16px;font-weight:700">THANK YOU</div>
  <div class="abs p w" style="left:236px;top:102px">For Your Attention</div>
</section>

</main>
</body>
</html>
```